Accommodation in an Executive Apartment for rent could be a Bed and breakfast,

Currently have a website and like the overall look but it needs revamping and want to add an instant booking button, which I would do later as the unit has a channel manager. Also want to be able to post blogs, etc. Need it to be viewed well on smart phones/tablets. all information related to this unit is on the current site which is www.lorvenstaysmirrabrook.com.au if you would view websites similar to staywell.example and roamtrip.example Must be able to be coded in Wordpress

The current design is done in Wordpress so would want this functionality in any new design.

Target Market(s)

Workers at Quorran precinct, Lorven. Workers at Halvern centre Mirrabrook, Workers at Marlow Peter Tenby Hospital, Workers at Brindlewood Hospital, Public Servants Woden, Workers in Mirrabrook ACT

Industry/Entity Type

Accommodation

Number of Pages Required

5+ page

Font styles to use
Sans Serif

Colors
ec1f27

Requirements
Must have
• Must have a classy look about it. Less clicks through the better. Not to wordy. Hard hitting points,
Nice to have
• Would like to retain the same colour theme and look
Should not have
• anything tacky

```html
<!DOCTYPE html>
<html lang="en">
<head>
<meta charset="utf-8">
<title>Lorven Bed &amp; Breakfast</title>
<link rel="stylesheet" href="https://fonts.googleapis.com/css2?family=Open+Sans:wght@400;600;700&family=Roboto+Condensed:wght@400;700&family=Arimo:wght@400;700&display=swap">
<style>
  :root {
    --red: #e5131d;
    --red-dark: #b3282c;
    --cream: #f0e8d8;
    --white: #ffffff;
    --text: #555555;
    --muted: #444444;
    --field-border: #c9c9c9;
  }
  * { box-sizing: border-box; margin: 0; padding: 0; }
  html, body { width: 1165px; height: 1200px; overflow: hidden; }
  body { background: var(--cream); font-family: "Open Sans", sans-serif; position: relative; }

  .hero {
    position: absolute; left: 0; top: 0; width: 1165px; height: 556px;
    background: linear-gradient(135deg, #8a6a4c 0%, #b8946e 30%, #d9c3a3 55%, #a7866a 80%, #6f5440 100%);
  }
  .hero-arrow {
    position: absolute; top: 292px; width: 38px; height: 38px; border-radius: 50%;
    background: rgba(60,40,30,0.35);
  }
  .hero-arrow svg { display: block; margin: 11px auto 0; }
  .hero-arrow.prev { left: 107px; }
  .hero-arrow.next { left: 1023px; }

  .site-header {
    position: absolute; left: 93px; top: 30px; width: 1072px; height: 70px;
    background: rgba(245,245,245,0.94);
  }
  .brand {
    position: absolute; left: 20px; top: 13px;
    font-family: "Open Sans", sans-serif; font-weight: 600; font-size: 34px; line-height: 44px;
    color: var(--red);
  }
  .main-nav, .footer-nav {
    position: absolute; display: flex; gap: 13px; list-style: none;
    font-family: "Roboto Condensed", sans-serif; font-size: 13.6px; color: var(--red);
  }
  .main-nav { left: 374px; top: 27px; }

  .card {
    position: absolute; top: 521px; width: 222px; height: 392px; background: var(--white);
  }
  .card-title {
    height: 71px; line-height: 70px; text-align: center;
    font-size: 16px; font-weight: 400; color: var(--red); text-transform: uppercase;
  }
  .card-photo { height: 215px; }
  .card-text {
    margin-top: 22px; padding: 0 16px; text-align: center;
    font-size: 12.5px; line-height: 16px; color: var(--muted);
  }
  .card-text .details { display: block; color: var(--red-dark); font-weight: 700; }
  .card.rooms { left: 94px; }
  .card.outdoors { left: 343px; }
  .card.nearby { left: 591px; height: 390px; }
  .card.nearby .card-photo { height: 211px; }
  .card.nearby .card-text { margin-top: 26px; }

  .guestbook { left: 835px; height: 390px; }
  .guestbook .card-title { height: 66px; line-height: 70px; }
  .field { position: absolute; left: 26px; width: 166px; }
  .field label {
    display: block; font-family: "Arimo", sans-serif; font-size: 12px; color: var(--muted); margin-bottom: 4px;
  }
  .field .input { height: 35px; border: 1px solid var(--field-border); background: var(--white); }
  .field .input.area { height: 57px; }
  .submit {
    position: absolute; left: 109px; top: 329px; width: 83px; height: 31px;
    background: var(--red-dark); color: var(--white); border: 0;
    font-family: "Arimo", sans-serif; font-weight: 700; font-size: 12px; text-transform: uppercase;
  }

  .welcome {
    position: absolute; left: 93px; top: 945px; width: 971px; height: 168px;
    background: var(--white); padding: 12px 15px;
  }
  .welcome h1 { font-size: 16.5px; font-weight: 600; color: var(--red); text-transform: uppercase; }
  .welcome p { margin-top: 12px; font-size: 14.4px; line-height: 19.4px; letter-spacing: -0.15px; color: var(--text); width: 945px; }

  .footer-nav { left: 93px; top: 1148px; }
  .copyright {
    position: absolute; left: 93px; top: 1170px;
    font-family: "Arimo", sans-serif; font-size: 11px; font-weight: 700; color: var(--muted);
  }
  .social { position: absolute; right: 101px; top: 1153px; display: flex; gap: 12px; list-style: none; }
  .social li { display: flex; align-items: center; gap: 5px; font-family: "Roboto Condensed", sans-serif; font-size: 13px; color: var(--muted); }
  .social .dot { width: 14px; height: 14px; background: #5a7fb0; }
</style>
</head>
<body>
  <div class="hero" role="img" aria-label="Sunlit living room with floral armchairs, red cushions and a white coffee table"></div>
  <div class="hero-arrow prev"><svg width="10" height="16" viewBox="0 0 10 16"><path d="M8 2 L2 8 L8 14" fill="none" stroke="#fff" stroke-width="3" opacity="0.7"/></svg></div>
  <div class="hero-arrow next"><svg width="10" height="16" viewBox="0 0 10 16"><path d="M2 2 L8 8 L2 14" fill="none" stroke="#fff" stroke-width="3" opacity="0.7"/></svg></div>

  <header class="site-header">
    <div class="brand">LORVEN</div>
    <ul class="main-nav">
      <li>HOME</li><li>B&amp;B ACCOMMODATION</li><li>GALLERY</li><li>WHAT'S NEARBY</li><li>GUEST BOOK</li><li>USEFUL LINKS</li><li>CONTACT US</li>
    </ul>
  </header>

  <section class="card rooms">
    <h2 class="card-title">Photos &amp; Rooms</h2>
    <div class="card-photo" role="img" aria-label="Bright bathroom with glass shower and vanity" style="background:linear-gradient(90deg,#b9bcbc,#e8e6e2 45%,#d9d4cc)"></div>
    <p class="card-text">Sed ut perspiciatis unde omnis iste natus err ipsa quae ab illo inventore veritatis et quasi <span class="details">Details</span></p>
  </section>

  <section class="card outdoors">
    <h2 class="card-title">The Outdoors</h2>
    <div class="card-photo" role="img" aria-label="Paved courtyard with garden table and shrubs" style="background:linear-gradient(160deg,#d9dccb,#5f6f3a 45%,#8a4c3c 80%,#6a3a2e)"></div>
    <p class="card-text">Sed ut perspiciatis unde omnis iste natus err ipsa quae ab illo inventore veritatis et quasi <span class="details">Details</span></p>
  </section>

  <section class="card nearby">
    <h2 class="card-title">What‘s Nearby</h2>
    <div class="card-photo" role="img" aria-label="Nearby centre lit up at dusk with steps and gardens" style="background:linear-gradient(180deg,#1f4fa8,#3a6cc4 35%,#5a6a5a 60%,#c9b89a 85%,#7a7a78)"></div>
    <p class="card-text">Sed ut perspiciatis unde omnis iste natus err ipsa quae ab illo inventore veritatis et quasi <span class="details">Details</span></p>
  </section>

  <section class="card guestbook">
    <h2 class="card-title">Guestbook</h2>
    <div class="field" style="top:62px"><label>Name</label><div class="input"></div></div>
    <div class="field" style="top:126px"><label>Email</label><div class="input"></div></div>
    <div class="field" style="top:189px"><label>Phone</label><div class="input"></div></div>
    <div class="field" style="top:249px"><label>Feedback</label><div class="input area"></div></div>
    <button class="submit">Submit</button>
  </section>

  <section class="welcome">
    <h1>Welcome to Lorven Bed &amp; Bredfast</h1>
    <p>Situated in the centrally located suburb of Mirrabrook this brand new Bed &amp; Breakfast features a separate bedroom and a spacious living area, a well equipped kitchen for self catering and in-unit laundry facilities.&nbsp; The apartment has it own private entrance with adjacent courtyard and off street parking, along with Vistacast and wireless internet, which will be available from 29th June 2012.&nbsp; Public transport is located within a 5 min walk.</p>
  </section>

  <ul class="footer-nav">
    <li>HOME</li><li>B&amp;B ACCOMMODATION</li><li>GALLERY</li><li>WHAT'S NEARBY</li><li>GUEST BOOK</li><li>USEFUL LINKS</li><li>CONTACT US</li>
  </ul>
  <div class="copyright">Copyrights 2015. All rights reserved. Terms &amp; Conditions</div>
  <ul class="social">
    <li><span class="dot"></span>Chatterly</li>
    <li><span class="dot"></span>Friendwall</li>
  </ul>
</body>
</html>
```